Wine label design for a family winery in Slovenia

We need new label design for our wines.
We are small family wine producers who focuses on good quality wine and loves to experiment, mixing tradition with new, more modern approaches. Our main product is ‘Teran’, red wine whose character is highly defined by terroir: more acidic, but rich body and very rich, dark colour (we say it's not red, but black). We also age a small portion of this Teran wine with wood, which we named 'Kamnje' (after one of our vineyards). From the same grapes as Teran we also produce a small quantity of Rose. And we also produce two white wine varieties: one is 'Zorn', cuvee of several different sorts of grapes. The other is 'Pečine', Chardonnay wine, named after another of our vineyards. Aside from all that we also produce liquour (Teranov liker) made from Teran wine and a small quantity of other spirits (Grappa, various fruit liquors, a version of Hügelbrand, and ‘Travarica’ which is grappa infused with various herbs and spices).
Zorn, Rose and Teran are considered our 'basic' line, whereas 'Kamnje' and 'Pečine' are considered to be a higher quality line. Rose sits somewhere between this two.
In time we'd like to renew all of our labels. But the priority and subject of this ‘’project’’ is to create the two for our top line, Kamnje and Pečine and also for Rose.
For 'Kamnje' we already have a template label. The general idea behind it was play with letters and divide them along the label (KA MN JE). We found that we like the narrow, longer dimensions and that black label on black bottle, with letters that stand out due to colour or printing differences, work very well. But we're amateurs and the label is not finalized. We would ask you to do something on this basis, but please don't limit yourself only to this if you have a better idea.
For 'Pečine' the label should be in the same style to imply the same higher quality line - colours can and probably should be reversed to the lighter side (so to imply that it’s a white wine). Also, for this wine we'll use the same dark slender bottles, like you see on the image.
Please keep in mind that we'll print smaller series (1000-2000 pcs), so it must be possible to print the labels for a sensible cost. Solutions like classical offset gold print that requires large series of 10.000 pcs, will not work. But we can look into any digital printing/lacquering options that offer similar effects. Anyway, we are not experts on this field, so your advice on printing techniques is also welcomed.
Also, a word on our emblem: the logo is also not finalized and we will also ask you to work on it. The logo is part of the ornament on the doors of our homestead and represents a ‘kolovrat’ (‘spinning wheel’ in English), an old Slavic symbol for the sun, representing eternal life and spinning of time. We'd like to use it, but right now it's badly digitalized. If you'll need any better photos of it, let me know.

Target Market(s)

30-60 yo, red wine lovers, appreciate local and speicality wines

Font styles to use
Sans Serif
Decorative

Requirements
Must have
• long, narrow label dimensions (see attached Kamnje)

```html
<!DOCTYPE html>
<html lang="sl">
<head>
<meta charset="utf-8">
<title>Brdska klet Vidmar — wine labels</title>
<link rel="stylesheet" href="https://fonts.googleapis.com/css2?family=Marcellus&family=Great+Vibes&display=swap">
<style>
  :root {
    --board-dark: #1c1c1c;
    --board-light: #ffffff;
    --label-black: #141414;
    --label-black-pattern: #1f1f1f;
    --label-white: #f4f4f4;
    --label-white-pattern: #e9e9e9;
    --label-pink: #f3c6c8;
    --label-pink-pattern: #f7d9da;
    --accent-red: #e2262c;
    --wine-red: #8a1b1b;
    --ink: #1a1a1a;
    --grey-on-black: #5a5a5a;
    --grey-on-white: #c9c9c9;
    --pink-soft: #efa3a7;
  }
  * { box-sizing: border-box; margin: 0; padding: 0; }
  html, body { width: 1200px; height: 2179px; overflow: hidden; }
  body { position: relative; background: var(--board-light); font-family: "Marcellus", serif; }

  .board-dark { position: absolute; left: 0; top: 0; width: 1200px; height: 1452px; background: var(--board-dark); }

  .label {
    position: absolute; width: 234px; height: 586px; overflow: hidden;
    display: flex; flex-direction: column; align-items: center;
  }
  .label--red { background: var(--label-black); color: #fff; }
  .label--white { background: var(--label-white); color: var(--ink); }
  .label--rose { background: var(--label-pink); color: var(--ink); }
  .label__pattern { position: absolute; inset: 0; }
  .label--red .label__pattern { background: radial-gradient(circle at 50% 40%, var(--label-black-pattern), var(--label-black)); }
  .label--white .label__pattern { background: radial-gradient(circle at 50% 40%, #fafafa, var(--label-white-pattern)); }
  .label--rose .label__pattern { background: radial-gradient(circle at 50% 40%, var(--label-pink-pattern), var(--label-pink)); }

  .brand { position: relative; display: flex; flex-direction: column; align-items: center; margin-top: 30px; }
  .brand__dot { width: 50px; height: 50px; border-radius: 50%; background: var(--wine-red); }
  .brand__name { margin-top: 12px; font-size: 15px; line-height: 16px; text-align: center; letter-spacing: .5px; }

  .wordbox {
    position: relative; margin-top: 60px; width: 197px; height: 162px;
    padding: 10px 12px; display: flex; flex-direction: column; justify-content: space-between;
  }
  .label--red .wordbox { border: 2px solid #444; }
  .label--white .wordbox { border: 2px solid #cfcfcf; background: rgba(255,255,255,.6); }
  .label--rose .wordbox { border: 2px solid #fff; background: rgba(255,255,255,.55); }
  .wordbox__row { display: flex; justify-content: space-between; font-size: 47px; line-height: 46px; }
  .label--red .dim { color: var(--grey-on-black); }
  .label--white .dim { color: var(--grey-on-white); }
  .label--rose .dim { color: var(--pink-soft); }
  .hot { color: var(--accent-red); }

  .variety { position: absolute; top: 578px; top: 508px; width: 100%; text-align: center; font-family: "Great Vibes", cursive; font-size: 16px; }
  .label--red .variety { color: #ddd; }
  .label--white .variety { color: #999; }
  .label--rose .variety { color: var(--accent-red); }

  .band {
    position: absolute; left: 0; top: 536px; width: 100%; height: 27px; background: var(--wine-red);
    color: #f2d9d9; font-size: 6.5px; letter-spacing: .6px; text-transform: uppercase;
    display: flex; align-items: center; justify-content: center;
  }

  .label--kamnje { left: 155px; top: 70px; }
  .label--pecine { left: 485px; top: 70px; }
  .label--rose-main { left: 815px; top: 70px; }

  .logo-card { position: absolute; left: 35px; top: 758px; width: 1130px; height: 658px; display: flex; align-items: center; justify-content: center; }
  .logo-card__pattern { position: absolute; inset: 0; background: radial-gradient(circle at 50% 45%, #ffffff, #ededed); }
  .logo-card__brand { position: relative; display: flex; flex-direction: column; align-items: center; }
  .logo-card__dot { width: 150px; height: 150px; border-radius: 50%; background: var(--wine-red); }
  .logo-card__name { margin-top: 26px; font-size: 46px; line-height: 46px; text-align: center; color: var(--ink); }

  .label--small { transform: scale(.5); transform-origin: 0 0; }
  .label--small-kamnje { left: 328px; top: 1710px; }
  .label--small-pecine { left: 538px; top: 1710px; }
  .label--small-rose { left: 746px; top: 1710px; }
</style>
</head>
<body>
  <div class="board-dark"></div>

  <!-- Kamnje -->
  <section class="label label--red label--kamnje">
    <div class="label__pattern" role="img" aria-label="Embossed swirling wheel pattern, black on black"></div>
    <div class="brand"><span class="brand__dot"></span><p class="brand__name">BRDSKA KLET<br>VIDMAR</p></div>
    <div class="wordbox">
      <div class="wordbox__row"><span class="hot">K</span><span class="hot">A</span><span class="dim">M</span><span class="dim">N</span></div>
      <div class="wordbox__row"><span class="dim">A</span><span class="hot">M</span><span class="hot">N</span><span class="hot">J</span></div>
      <div class="wordbox__row"><span class="dim">M</span><span class="dim">N</span><span class="hot">J</span><span class="hot">E</span></div>
    </div>
    <p class="variety">Lorem Ipsum Dolor</p>
    <p class="band">Alc. 12% | Bottled in Slovenia | 750 ml</p>
  </section>

  <!-- Pečine -->
  <section class="label label--white label--pecine">
    <div class="label__pattern" role="img" aria-label="Embossed swirling wheel pattern, white on light grey"></div>
    <div class="brand"><span class="brand__dot"></span><p class="brand__name">BRDSKA KLET<br>VIDMAR</p></div>
    <div class="wordbox">
      <div class="wordbox__row"><span class="hot">P</span><span class="hot">E</span><span class="dim">Č</span><span class="dim">I</span></div>
      <div class="wordbox__row"><span class="dim">E</span><span class="hot">Č</span><span class="hot">I</span><span class="hot">N</span></div>
      <div class="wordbox__row"><span class="dim">Č</span><span class="dim">I</span><span class="hot">N</span><span class="hot">E</span></div>
    </div>
    <p class="variety">Chardonnay</p>
    <p class="band">Alc. 12% | Bottled in Slovenia | 750 ml</p>
  </section>

  <!-- Rosé -->
  <section class="label label--rose label--rose-main">
    <div class="label__pattern" role="img" aria-label="Embossed swirling wheel pattern, pale pink"></div>
    <div class="brand"><span class="brand__dot"></span><p class="brand__name">BRDSKA KLET<br>VIDMAR</p></div>
    <div class="wordbox">
      <div class="wordbox__row"><span class="hot">R</span><span class="dim">O</span><span class="dim">S</span><span class="dim">É</span></div>
      <div class="wordbox__row"><span class="dim">R</span><span class="hot">O</span><span class="dim">S</span><span class="dim">É</span></div>
      <div class="wordbox__row"><span class="dim">R</span><span class="dim">O</span><span class="hot">S</span><span class="hot">É</span></div>
    </div>
    <p class="variety">Rosé</p>
    <p class="band">Alc. 12% | Bottled in Slovenia | 750 ml</p>
  </section>

  <!-- Brand card -->
  <section class="logo-card">
    <div class="logo-card__pattern" role="img" aria-label="Embossed swirling wheel pattern, white on white"></div>
    <div class="logo-card__brand">
      <span class="logo-card__dot"></span>
      <p class="logo-card__name">BRDSKA KLET<br>VIDMAR</p>
    </div>
  </section>

  <!-- Label range, small -->
  <section class="label label--red label--small label--small-kamnje">
    <div class="label__pattern" role="img" aria-label="Embossed swirling wheel pattern, black on black"></div>
    <div class="brand"><span class="brand__dot"></span><p class="brand__name">BRDSKA KLET<br>VIDMAR</p></div>
    <div class="wordbox">
      <div class="wordbox__row"><span class="hot">K</span><span class="hot">A</span><span class="dim">M</span><span class="dim">N</span></div>
      <div class="wordbox__row"><span class="dim">A</span><span class="hot">M</span><span class="hot">N</span><span class="hot">J</span></div>
      <div class="wordbox__row"><span class="dim">M</span><span class="dim">N</span><span class="hot">J</span><span class="hot">E</span></div>
    </div>
    <p class="variety">Lorem Ipsum Dolor</p>
    <p class="band">Alc. 12% | Bottled in Slovenia | 750 ml</p>
  </section>

  <section class="label label--white label--small label--small-pecine">
    <div class="label__pattern" role="img" aria-label="Embossed swirling wheel pattern, white on light grey"></div>
    <div class="brand"><span class="brand__dot"></span><p class="brand__name">BRDSKA KLET<br>VIDMAR</p></div>
    <div class="wordbox">
      <div class="wordbox__row"><span class="hot">P</span><span class="hot">E</span><span class="dim">Č</span><span class="dim">I</span></div>
      <div class="wordbox__row"><span class="dim">E</span><span class="hot">Č</span><span class="hot">I</span><span class="hot">N</span></div>
      <div class="wordbox__row"><span class="dim">Č</span><span class="dim">I</span><span class="hot">N</span><span class="hot">E</span></div>
    </div>
    <p class="variety">Chardonnay</p>
    <p class="band">Alc. 12% | Bottled in Slovenia | 750 ml</p>
  </section>

  <section class="label label--rose label--small label--small-rose">
    <div class="label__pattern" role="img" aria-label="Embossed swirling wheel pattern, pale pink"></div>
    <div class="brand"><span class="brand__dot"></span><p class="brand__name">BRDSKA KLET<br>VIDMAR</p></div>
    <div class="wordbox">
      <div class="wordbox__row"><span class="hot">R</span><span class="dim">O</span><span class="dim">S</span><span class="dim">É</span></div>
      <div class="wordbox__row"><span class="dim">R</span><span class="hot">O</span><span class="dim">S</span><span class="dim">É</span></div>
      <div class="wordbox__row"><span class="dim">R</span><span class="dim">O</span><span class="hot">S</span><span class="hot">É</span></div>
    </div>
    <p class="variety">Rosé</p>
    <p class="band">Alc. 12% | Bottled in Slovenia | 750 ml</p>
  </section>
</body>
</html>
```